Flyer for a 1 day conference event - with our design elements

We need a two sided A4 flyer created for our 1 day conference, using our corporate design elements.

It is an exclusive event for high profile professional speakers, and it's important for the flyer to be engaging, professional and clean.

We want the prospective attendees to see how much value there is in the day and to feel the event cannot be missed.

I will need to be able to make small edits back and forth with the successful designer in order to get it just-right. (ie: It won't work if I only get access to 2-3 revisions... but don't worry - I don't intend to request an entire re-design)

Target Market(s)

High profile professional speakers

Industry/Entity Type

Event

Requirements
Must have
• Not too much clutter. Some of own design elements
Nice to have
• A large image/photo. Doesnt have to be of a microphone or stage or curtain (traditional speaker things) .. it could be something 'spring' like because it being held in Spring.
Should not have
• too many colours. too many different fonts. too much clutter.

```html
<!DOCTYPE html>
<html lang="en">
<head>
<meta charset="utf-8">
<title>Debate and Dissent – Immediate Insight</title>
<link href="https://fonts.googleapis.com/css2?family=Roboto+Condensed:wght@400;700&display=swap" rel="stylesheet">
<style>
  :root{
    --navy:#163f86;
    --royal:#1d5cb0;
    --heading:#1b4e9e;
    --ink:#0e2048;
    --white:#ffffff;
  }
  *{margin:0;padding:0;box-sizing:border-box}
  html,body{width:848px;height:1200px;overflow:hidden;background:#fff}
  body{font-family:"Roboto Condensed", "Arial Narrow", sans-serif;color:var(--ink)}
  .flyer{position:relative;width:848px;height:1200px;overflow:hidden}
  .backdrop{position:absolute;inset:0}
  .brand{position:absolute;left:60px;top:20px;display:flex;align-items:center;gap:10px}
  .brand-mark{width:26px;height:26px;border-radius:50%;background:var(--navy)}
  .brand-text{font-weight:700;color:var(--navy);font-size:21px;line-height:1.05}
  .brand-tagline{font-weight:700;color:var(--navy);font-size:13px}
  .speaker-photo{position:absolute;left:30px;top:135px;width:250px;height:420px;border-radius:4px;
    background:linear-gradient(160deg,#cfe7f6 0%,#9c7a55 45%,#2b2f3a 75%,#1c2230 100%)}
  .section-title{position:absolute;color:var(--heading);font-weight:400;line-height:1;white-space:nowrap}
  .title-debate{left:365px;top:150px;font-size:42px}
  .subtitle-debate{left:292px;top:196px;font-size:39px}
  .title-insight{left:279px;top:690px;font-size:38px}
  .subtitle-insight{left:197px;top:735px;font-size:38px}
  .block{position:absolute;font-size:17px}
  .block h3{font-weight:400;font-size:17px}
  .block .item{margin-bottom:22px}
  .lead-debate{left:428px;top:240px;font-size:21px;line-height:1;font-weight:400}
  .debate-body{left:331px;top:262px;width:490px;line-height:21.5px}
  .insight-body{left:208px;top:779px;width:625px;line-height:23px}
  .contact{position:absolute;left:238px;top:1146px;color:var(--white);font-size:29px;white-space:nowrap}
</style>
</head>
<body>
<main class="flyer">
  <svg class="backdrop" width="848" height="1200" viewBox="0 0 848 1200" aria-hidden="true">
    <defs>
      <linearGradient id="sky" x1="0" y1="0" x2="0.3" y2="1">
        <stop offset="0" stop-color="#e6f6fd"/>
        <stop offset="0.45" stop-color="#a9dcf6"/>
        <stop offset="1" stop-color="#5fb2e6"/>
      </linearGradient>
      <radialGradient id="glow" cx="0.5" cy="0.5" r="0.5">
        <stop offset="0" stop-color="#fff" stop-opacity=".55"/>
        <stop offset="1" stop-color="#fff" stop-opacity="0"/>
      </radialGradient>
    </defs>
    <rect width="848" height="1200" fill="url(#sky)"/>
    <circle cx="640" cy="330" r="200" fill="url(#glow)"/>
    <circle cx="470" cy="950" r="220" fill="url(#glow)"/>
    <path d="M520 0 C640 30 760 40 848 20 L848 0 Z" fill="#2a6fc2"/>
    <path d="M600 0 C700 50 790 80 848 120 L848 0 Z" fill="#1d56a8" opacity=".9"/>
    <path d="M700 0 C760 70 810 140 848 210 L848 0 Z" fill="#3f8fd8" opacity=".6"/>
    <path d="M0 420 C60 600 120 820 170 1200 L0 1200 Z" fill="#3d8fd6" opacity=".55"/>
    <path d="M0 560 C50 740 100 920 130 1200 L0 1200 Z" fill="#1f5fb2"/>
    <path d="M0 700 C30 860 60 1020 80 1200 L0 1200 Z" fill="#163f86"/>
    <path d="M150 1200 C300 1080 600 1040 848 1000 L848 1200 Z" fill="#2e7ccd" opacity=".35"/>
    <path d="M110 1126 C300 1118 600 1116 848 1120 L848 1200 L100 1200 Z" fill="var(--royal)"/>
  </svg>

  <header class="brand">
    <span class="brand-mark"></span>
    <div>
      <div class="brand-text">Podium Guild<br>of Australia</div>
      <div class="brand-tagline">Voices With Substance</div>
    </div>
  </header>

  <div class="speaker-photo" role="img" aria-label="Photo of a speaker in a dark suit leaning on a wooden lectern"></div>

  <h1 class="section-title title-debate">DEBATE AND DISSENT ::</h1>
  <h2 class="section-title subtitle-debate">Let’s get some friction and sport.</h2>
  <h3 class="block lead-debate">Thumbite Debates</h3>

  <section class="block debate-body">
    <p class="item">Three affirmative, three negative, one minute per person – go.</p>
    <div class="item">
      <p>Topics will be generated on the day and may include:</p>
      <p>That motivational speakers were responsible for the GFC.</p>
      <p>The the PGA has lost its way.</p>
      <p>That bureaus are underappreciated.</p>
      <p>That it is too easy to become a CSP.</p>
      <p>That ego has no place in speaking.</p>
    </div>
    <div class="item">
      <h3>Help Me Hypothetically</h3>
      <p>Anonymous submissions of ethical challenges receive responses and we discuss.</p>
    </div>
    <div class="item">
      <h3>Telling People What They Don’t Want To Hear</h3>
      <p>Three people will each present a difficult truth to a hostile audience while we explore ways of delivering more confronting, provocative or unpopular ideas and how we might better deal with dissent or discomfort in the room.</p>
    </div>
  </section>

  <h1 class="section-title title-insight">IMMEDIATE INSIGHT ::</h1>
  <h2 class="section-title subtitle-insight">Share what you know or see, fast.</h2>

  <section class="block insight-body">
    <div class="item">
      <h3>Blow My Trumpet For Me</h3>
      <p>Get your promotional copy written by three other people. What does it say? What does it tell you? What do you learn?</p>
    </div>
    <div class="item">
      <h3>Emergency Presentation</h3>
      <p>You are put into small groups – crack teams – to prepare a keynote from various criteria. Ten minutes to prepare. Five minutes to present your outline.</p>
    </div>
    <div class="item">
      <h3>Instant Unedited Product Review</h3>
      <p>Get a super-efficient, ruthless critique of one of your products.</p>
    </div>
    <div class="item">
      <h3>Show Me The Future</h3>
      <p>Webinar, ClipHub, Circlely, Blogging, Chirper, podcasts and ebooks – what is going on? Which are you doing? Which are you resisting or declining? What’s next?</p>
    </div>
  </section>

  <p class="contact">Contact Marcus to discuss: marcus@lindqvale.com</p>
</main>
</body>
</html>
```